Venlox - Property Management Company Listings - PSD / uncoded only

Our site simply connects property owners with property managers. I’m asking you to create 2 pages, 1 homepage and 1 page that lists of property management companies. Build with Responsive Design in mind. PSD/uncoded files only. Help us create a great site!
Example competitor sites:
http://www.everyestatehelp.example/
http://www.tendyourlots.example/
Inspired by these sites:
http://www.quorvik.example/
http://www.bespokely.example/
http://www.coinwire.example/
https://www.tripboard.example/
I've attached the logo as well as 2 picture files that you can consider using.
• Venlox Logo Colors: Yellow: HTML code: #FBC30A, RGB code: R: 251 G: 195 B: 10 Grey: HTML code: #4E4C4D, RGB code: R: 78 G: 76 B: 77
• The picture files are optional.
o One picture is of houses and neighborhood.
o The other is of a professional woman on the phone. Please do not use the professional woman as a large primary image. You can use the professional woman photo as a smaller photo and not the main photo.
• Please bring your own pictures and graphics too. Don't feel like you need to use mine.
Thank you!

```html
<!DOCTYPE html>
<html lang="en">
<head>
<meta charset="utf-8">
<title>Venlox — Property Management Solutions Simplified</title>
<link href="https://fonts.googleapis.com/css2?family=Open+Sans:wght@300;400;600;700&display=swap" rel="stylesheet">
<style>
  :root {
    --brand-yellow: #FBC30A;
    --brand-grey: #4E4C4D;
    --ink: #333333;
    --ink-soft: #4a4a4a;
    --page-bg: #f3f3f3;
    --panel-grey: #c9c9c9;
    --footer-bg: #2b2b2b;
    --white: #ffffff;
  }
  * { box-sizing: border-box; margin: 0; padding: 0; }
  html, body { width: 1069px; height: 1200px; overflow: hidden; }
  body {
    position: relative;
    font-family: "Open Sans", Arial, sans-serif;
    color: var(--ink);
    background: var(--page-bg);
  }

  /* Utility bar */
  .utility-bar {
    position: absolute; top: 0; left: 0; width: 1069px; height: 23px;
    background: var(--brand-yellow);
    font-size: 13px; color: var(--ink);
  }
  .utility-link { position: absolute; top: 3px; display: flex; align-items: center; gap: 8px; }
  .utility-link svg { width: 12px; height: 12px; fill: var(--ink); }
  .utility-login { left: 846px; }
  .utility-phone { left: 928px; }

  /* Header */
  .site-header {
    position: absolute; top: 23px; left: 0; width: 1069px; height: 69px;
    background: var(--white);
  }
  .brand { position: absolute; left: 44px; top: 20px; display: flex; align-items: center; gap: 5px; }
  .brand-mark { width: 10px; height: 10px; background: var(--brand-yellow); }
  .brand-name { font-size: 24px; font-weight: 700; color: var(--brand-grey); line-height: 1; letter-spacing: -0.3px; }
  .brand-tagline {
    position: absolute; left: 154px; top: 14px;
    font-size: 17.5px; font-weight: 400; color: var(--ink); line-height: 20px;
  }
  .brand-tagline span { display: block; padding-left: 8px; font-weight: 600; font-size: 16.5px; }
  .main-nav { position: absolute; top: 25px; left: 0; font-size: 15.5px; color: var(--ink); }
  .main-nav a { position: absolute; white-space: nowrap; color: inherit; text-decoration: none; }

  /* Hero */
  .hero {
    position: absolute; top: 92px; left: 0; width: 1069px; height: 424px;
    background: linear-gradient(160deg, #6f7c86 0%, #8c8a80 35%, #6d7f4e 60%, #8e8678 80%, #5f6a72 100%);
  }
  .hero-caption {
    position: absolute; top: 114px; left: 0; width: 636px; height: 60px;
    background: rgba(40, 40, 40, 0.55);
    color: var(--brand-yellow); font-size: 19.8px;
    padding: 15px 0 0 72px; white-space: nowrap;
  }

  /* Manager invitation */
  .manager-pitch { position: absolute; top: 540px; left: 0; width: 1069px; text-align: center; }
  .manager-pitch h1 {
    font-size: 29px; font-weight: 400; letter-spacing: 1px; color: var(--ink);
  }
  .manager-pitch p {
    margin-top: 26px; font-size: 21.2px; font-weight: 300; line-height: 30px; color: var(--ink-soft);
  }
  .btn {
    display: inline-flex; align-items: center; justify-content: center; gap: 12px;
    background: var(--brand-yellow); color: var(--ink);
    font-size: 20px; font-weight: 300; text-decoration: none;
  }
  .btn svg { width: 12px; height: 14px; fill: var(--ink); }
  .btn-learn { margin-top: 26px; width: 144px; height: 40px; }

  /* Cards */
  .card {
    position: absolute; top: 761px; height: 291px;
    border: 2px solid var(--brand-yellow);
  }
  .card-search { left: 36px; width: 488px; background: var(--panel-grey); padding: 26px 27px; }
  .card-steps { left: 545px; width: 487px; background: var(--white); padding: 24px 19px; }
  .card h2 { font-size: 18.8px; font-weight: 400; color: var(--ink); line-height: 25px; }
  .search-fields { display: flex; gap: 8px; margin-top: 20px; }
  .field label { display: block; font-size: 16px; margin-bottom: 8px; }
  .field-type { width: 259px; }
  .field-zip { width: 162px; }
  .select-box, .input-box {
    height: 38px; background: var(--white); border: 1px solid #555;
    font-size: 12.6px; display: flex; align-items: center; padding-left: 4px; position: relative;
    white-space: nowrap;
  }
  .select-box svg { position: absolute; right: 6px; top: 16px; width: 10px; height: 6px; fill: #444; }
  .btn-search { display: flex; margin: 26px 0 0 159px; width: 126px; height: 35px; }
  .btn-search svg { width: 14px; height: 14px; fill: none; stroke: var(--ink); }
  .card-search .note { margin-top: 15px; font-size: 15.5px; line-height: 20px; color: var(--ink-soft); }
  .steps { list-style: none; margin-top: 22px; font-size: 14px; color: var(--ink-soft); }
  .steps li { height: 34px; }
  .btn-find { display: flex; margin: 20px 0 0 149px; width: 144px; height: 40px; }

  /* Footer */
  .site-footer {
    position: absolute; top: 1129px; left: 0; width: 1069px; height: 71px;
    background: var(--footer-bg); border-top: 2px solid var(--brand-yellow);
  }
  .copyright { position: absolute; left: 64px; top: 32px; font-size: 11px; color: var(--white); }
  .footer-links { position: absolute; left: 592px; top: 23px; width: 440px; list-style: none;
    display: flex; flex-wrap: wrap; row-gap: 2px; font-size: 11px; }
  .footer-links li { display: flex; align-items: center; margin-right: 10px; }
  .footer-links li::before {
    content: ""; width: 6px; height: 6px; border-radius: 50%; background: var(--white); margin-right: 9px;
  }
  .footer-links a { color: var(--brand-yellow); text-decoration: none; }
</style>
</head>
<body>

  <div class="utility-bar">
    <span class="utility-link utility-login">
      <svg viewBox="0 0 12 12"><circle cx="6" cy="3.2" r="2.8"/><path d="M0.5 12 C0.5 7.5 11.5 7.5 11.5 12 Z"/></svg>
      Login
    </span>
    <span class="utility-link utility-phone">
      <svg viewBox="0 0 12 12"><path d="M2.3 0.5 L4.3 3.2 L3.1 4.6 C3.8 6.2 5.6 8.1 7.3 8.9 L8.7 7.6 L11.5 9.6 L10.1 11.5 C5 11.2 0.8 7 0.5 1.9 Z"/></svg>
      555 014 2290
    </span>
  </div>

  <header class="site-header">
    <div class="brand">
      <span class="brand-mark"></span>
      <span class="brand-name">Venlox</span>
    </div>
    <div class="brand-tagline">Property Management Solutions<span>Simplified.</span></div>
    <nav class="main-nav">
      <a href="#" style="left:646px">Home</a>
      <a href="#" style="left:713px">Are you a Property&nbsp; Manager</a>
      <a href="#" style="left:940px">Contact Us</a>
    </nav>
  </header>

  <section class="hero" role="img" aria-label="Aerial photograph of a suburban neighbourhood of family houses with lawns and trees">
    <div class="hero-caption">Making renting YOUR home an easy, stress-free experience.</div>
  </section>

  <section class="manager-pitch">
    <h1>ARE YOU A PROPERTY MANAGER?</h1>
    <p>Join our real estate property management company network.<br>Let us help you find leads of property owners seeking to rent their homes</p>
    <a class="btn btn-learn" href="#">Learn More <svg viewBox="0 0 12 14"><path d="M0 0 L12 7 L0 14 Z"/></svg></a>
  </section>

  <section class="card card-search">
    <h2>Find your Local Property Manager</h2>
    <div class="search-fields">
      <div class="field field-type">
        <label>Select Property Type:</label>
        <div class="select-box">Single Home or Condo ($300 to $500K)
          <svg viewBox="0 0 10 6"><path d="M0 0 L10 0 L5 6 Z"/></svg>
        </div>
      </div>
      <div class="field field-zip">
        <label>In Zipcode:</label>
        <div class="input-box"></div>
      </div>
    </div>
    <a class="btn btn-search" href="#">Search
      <svg viewBox="0 0 14 14" stroke-width="2.2"><circle cx="5.8" cy="5.8" r="4.4"/><path d="M9 9 L13 13" stroke-linecap="round"/></svg>
    </a>
    <p class="note">Search our directory to find experienced and professional property management companies that meet your needs.</p>
  </section>

  <section class="card card-steps">
    <h2>Three steps To find property management companies near you:</h2>
    <ul class="steps">
      <li>Select your property type and zipcode</li>
      <li>Review property manager listings in your area</li>
      <li>Select and compare property managers</li>
    </ul>
    <a class="btn btn-find" href="#">Find Now <svg viewBox="0 0 12 14"><path d="M0 0 L12 7 L0 14 Z"/></svg></a>
  </section>

  <footer class="site-footer">
    <p class="copyright">Copyright © 2014, Venlox, All Rights Reserved</p>
    <ul class="footer-links">
      <li><a href="#">Are you a Property Manager?</a></li>
      <li><a href="#">About Us</a></li>
      <li><a href="#">Contact Us</a></li>
      <li><a href="#">Terms of Use</a></li>
      <li><a href="#">Privacy Policy</a></li>
      <li><a href="#">Sitemap</a></li>
    </ul>
  </footer>

</body>
</html>
```